Marwood Holiday Jubilee 2025

We’re looking for a designer to help refresh the visual identity of our annual Christmas show while maintaining continuity from previous years. The updated design should feel festive, and warm, with a sense of celebration and anticipation. We’d like a central graphic that can be adapted for posters, social media, and digital signage, along with supporting assets for flyers and banners.

We’re open to seasonal color palettes such as rich reds, deep greens or blues, golds, silvers, or cool winter tones, and prefer typography that’s clear and elegant. The overall look should feel familiar to returning audiences while inviting and engaging for newcomers.

Two key groups: the current attenders of our congregation and the broader community in our suburb of Rochester, NY. Our congregation is made up of families, older adults, and young professionals who value faith, community and spiritual growth. The surrounding community is a fast growing friendly and family-oriented area of young professionals and longtime families.

We’re looking for a designer to help refresh the visual identity of our annual Christmas show while maintaining continuity with the theme and tone of previous years. The updated design should feel festive, and warm, with a sense of celebration and anticipation. We’d like a central graphic that can be adapted for posters, social media, and digital signage, along with supporting assets for flyers and banners.

Target Market(s)

Two key groups: the current attenders of our congregation and the broader community in our suburb of Rochester, NY. Our congregation is made up of families, older adults, and young professionals who value faith, community and spiritual growth. The surrounding community is a fast growing friendly and family-oriented area of young professionals and long time families.

Industry/Entity Type

Non-profit. Church

Font styles to use
Serif
Decorative
Script
Other font styles liked:
• Quentin

Requirements
Must have
• Sparkle, eye catching
Should not have
• must not look identical to the uploaded versions

```html
<!DOCTYPE html>
<html lang="en">
<head>
<meta charset="utf-8">
<title>Marwood Holiday Jubilee</title>
<link rel="stylesheet" href="https://fonts.googleapis.com/css2?family=Josefin+Sans:wght@500;600&family=Montserrat:wght@600;700&family=Allura&display=swap">
<style>
  :root {
    --page: #949494;
    --night-top: #0a2650;
    --night-mid: #123f6a;
    --glow: #3a8fb0;
    --glow-soft: rgba(110,190,215,0.5);
    --ground: #1d5379;
    --ground-deep: #0a1730;
    --gold-light: #f8cf76;
    --gold: #e3a43c;
    --gold-deep: #b8741f;
    --spark: #ffffff;
  }
  * { margin: 0; padding: 0; box-sizing: border-box; }
  html, body {
    width: 1200px; height: 1200px; overflow: hidden;
    background: var(--page);
  }
  .banner {
    position: absolute; left: 67px; top: 270px;
    width: 1066px; height: 660px;
    overflow: hidden;
  }
  .winter-scene {
    position: absolute; inset: 0;
    background:
      radial-gradient(circle at 50.5% 26%, rgba(255,255,255,0.75) 0, rgba(170,220,240,0.35) 3%, transparent 12%),
      radial-gradient(ellipse 20% 65% at 50.5% 55%, var(--glow-soft), transparent 72%),
      radial-gradient(ellipse 28% 45% at 82% 25%, rgba(70,150,180,0.35), transparent 70%),
      linear-gradient(180deg, transparent 0 80%, var(--ground) 81.5%, var(--ground-deep) 100%),
      linear-gradient(180deg, var(--night-top) 0%, var(--night-mid) 55%, var(--glow) 80%);
  }
  .gold {
    background: linear-gradient(180deg, var(--gold-light) 0%, var(--gold) 50%, var(--gold-deep) 100%);
    -webkit-background-clip: text; background-clip: text;
    color: transparent;
    filter: drop-shadow(0 0 6px rgba(246,190,90,0.35));
  }
  .host {
    position: absolute; left: 20px; top: 268px; width: 420px;
    text-align: center;
    font-family: "Josefin Sans", sans-serif; font-weight: 600;
    font-size: 31px; line-height: 38px; letter-spacing: 2.5px;
  }
  .presents {
    position: absolute; left: 52px; top: 364px; width: 366px;
    display: flex; align-items: center; gap: 10px;
  }
  .presents .rule { flex: 1; height: 1.5px; background: var(--gold); }
  .presents .word {
    font-family: "Allura", cursive; font-size: 50px; line-height: 1;
    color: var(--gold);
  }
  .title {
    position: absolute; left: 610px; top: 232px; width: 456px;
    text-align: center;
    font-family: "Montserrat", sans-serif; font-weight: 700;
    font-size: 62px; line-height: 58px; letter-spacing: 4px;
  }
  .title-script {
    position: absolute; left: 610px; top: 340px; width: 456px;
    text-align: center;
    font-family: "Allura", cursive; font-size: 96px; line-height: 92px;
  }
  .dates {
    position: absolute; left: 610px; top: 440px; width: 456px;
    text-align: center;
    font-family: "Montserrat", sans-serif; font-weight: 600;
    font-size: 16px; letter-spacing: 2px; color: var(--gold);
  }
  .glint {
    position: absolute; width: 30px; height: 30px;
    margin: -15px 0 0 -15px;
    filter: drop-shadow(0 0 4px var(--spark)) drop-shadow(0 0 8px rgba(255,230,170,0.8));
  }
  .glint path { fill: var(--spark); }
  .glint.small { width: 20px; height: 20px; margin: -10px 0 0 -10px; }
</style>
</head>
<body>
  <div class="banner">
    <div class="winter-scene" role="img" aria-label="Starry night sky over a snowy pine forest with a glowing lit Christmas tree topped by a bright star at the centre"></div>

    <div class="host gold">MAPLE HOLLOW<br>COMMUNITY CHURCH</div>
    <div class="presents">
      <span class="rule"></span>
      <span class="word">presents</span>
      <span class="rule"></span>
    </div>

    <h1 class="title gold">MARWOOD<br>HOLIDAY</h1>
    <div class="title-script gold">Jubilee</div>
    <p class="dates">DECEMBER 16 &amp; 17. 6:00 PM</p>

    <svg class="glint" style="left:304px;top:292px" viewBox="0 0 30 30" aria-hidden="true"><path d="M15 0 L16.2 13.8 L30 15 L16.2 16.2 L15 30 L13.8 16.2 L0 15 L13.8 13.8 Z"/></svg>
    <svg class="glint small" style="left:160px;top:329px" viewBox="0 0 30 30" aria-hidden="true"><path d="M15 0 L16.2 13.8 L30 15 L16.2 16.2 L15 30 L13.8 16.2 L0 15 L13.8 13.8 Z"/></svg>
    <svg class="glint small" style="left:361px;top:329px" viewBox="0 0 30 30" aria-hidden="true"><path d="M15 0 L16.2 13.8 L30 15 L16.2 16.2 L15 30 L13.8 16.2 L0 15 L13.8 13.8 Z"/></svg>
    <svg class="glint" style="left:955px;top:318px" viewBox="0 0 30 30" aria-hidden="true"><path d="M15 0 L16.2 13.8 L30 15 L16.2 16.2 L15 30 L13.8 16.2 L0 15 L13.8 13.8 Z"/></svg>
    <svg class="glint" style="left:748px;top:378px" viewBox="0 0 30 30" aria-hidden="true"><path d="M15 0 L16.2 13.8 L30 15 L16.2 16.2 L15 30 L13.8 16.2 L0 15 L13.8 13.8 Z"/></svg>
  </div>
</body>
</html>
```